7Brink Plumbing flyer

I want to incorporate our logo design into a new flyer promoting the business and advertising products that we install.
We install hot water systems, Air-conditioning systems and central heating systems. Along with other aspects of plumbing such as gasfitting, roofing, sanitary and drainage
I would like the background to be the same as our business cards with the water effect and colours.

Requirements
Must have
• Logo
24/7 Emergency call out
Aspects of plumbing we do
- Hot water systems
- Central Heating
- Solar hot water systems/ heat pump systems
- Gasfitting
- Drainage
- Roofing
- Air-Conditioning
Nice to have
• Pictures of hot water systems and air-conditioning system
$30 off voucher when producing this flyer (limit 1 per house hold)

```html
<!DOCTYPE html>
<html lang="en">
<head>
<meta charset="utf-8">
<title>7Brink Plumbing – Flyer</title>
<link href="https://fonts.googleapis.com/css2?family=Orbitron:wght@700;800&family=Oswald:wght@600&family=Catamaran:wght@400;500&display=swap" rel="stylesheet">
<style>
  :root{
    --page:#dcdde0;
    --dark:#2b2c2f;
    --dark-deep:#1f2022;
    --blue:#0a7fc8;
    --blue-deep:#0564ad;
    --blue-light:#0eaeea;
    --ink:#2d2d2d;
    --footer:#f0f1f2;
    --white:#ffffff;
  }
  html,body{margin:0;padding:0;width:1145px;height:1200px;overflow:hidden;background:var(--page);}
  .flyer{position:absolute;left:162px;top:20px;width:820px;height:1160px;box-shadow:0 18px 40px rgba(0,0,0,.22);}
  .flyer svg{display:block;}
  .brand{font-family:"Orbitron",sans-serif;font-weight:800;fill:var(--blue-light);}
  .brand-sub{font-family:"Orbitron",sans-serif;font-weight:700;fill:#dbe9f3;}
  .display{font-family:"Orbitron",sans-serif;font-weight:800;}
  .callout{font-family:"Oswald",sans-serif;font-weight:600;fill:var(--white);font-size:30px;}
  .body{font-family:"Catamaran",sans-serif;fill:var(--ink);}
  .service{font-family:"Catamaran",sans-serif;font-size:21px;fill:#3a3a3a;}
  .contact{font-family:"Catamaran",sans-serif;font-size:16px;fill:#3a3a3a;}
</style>
</head>
<body>
<div class="flyer">
<svg width="820" height="1160" viewBox="0 0 820 1160" xmlns="http://www.w3.org/2000/svg">
  <defs>
    <linearGradient id="blueBand" x1="0" y1="0" x2="1" y2="1">
      <stop offset="0" stop-color="#0eaeea"/>
      <stop offset="0.55" stop-color="#0a86d0"/>
      <stop offset="1" stop-color="#0564ad"/>
    </linearGradient>
    <linearGradient id="darkBg" x1="0" y1="0" x2="0" y2="1">
      <stop offset="0" stop-color="#333438"/>
      <stop offset="1" stop-color="#242528"/>
    </linearGradient>
    <linearGradient id="dome" x1="0" y1="0" x2="1" y2="1">
      <stop offset="0" stop-color="#0a86d0"/>
      <stop offset="1" stop-color="#0564ad"/>
    </linearGradient>
    <clipPath id="headerClip">
      <path d="M0,0 H820 V395 C600,490 330,490 200,472 C120,462 60,450 0,437 Z"/>
    </clipPath>
  </defs>

  <!-- page base -->
  <rect class="base" width="820" height="1160" fill="var(--white)"/>

  <!-- blue emergency band -->
  <path class="band-blue" d="M0,430 C200,480 500,500 820,385 V635 C680,648 530,648 440,668 H0 Z" fill="url(#blueBand)"/>
  <path class="band-white-left" d="M0,482 C120,505 240,500 330,495 L330,700 L0,700 Z" fill="var(--white)"/>
  <path class="band-edge" d="M440,668 C560,645 700,636 820,628 V648 C700,656 560,668 470,684 Z" fill="var(--dark-deep)"/>

  <!-- dark header -->
  <path class="header-dark" d="M0,0 H820 V395 C600,490 330,490 200,472 C120,462 60,450 0,437 Z" fill="url(#darkBg)"/>

  <!-- technician photo area, cut by the wave -->
  <g clip-path="url(#headerClip)">
    <rect class="photo-technician" role="img" aria-label="Photo of a smiling plumber in overalls holding a pipe wrench" x="523" y="39" width="265" height="460" rx="6" fill="#5a3a45" opacity="0.85"/>
  </g>
  <path class="header-rule" d="M190,480 C330,498 600,492 820,402" fill="none" stroke="var(--white)" stroke-width="7"/>

  <!-- brand block -->
  <circle class="brand-mark" cx="270" cy="107" r="44" fill="var(--blue-light)"/>
  <text class="brand" x="85" y="247" font-size="62" textLength="379" lengthAdjust="spacingAndGlyphs">7BRINK</text>
  <text class="brand" x="85" y="299" font-size="46" textLength="379" lengthAdjust="spacingAndGlyphs">PLUMBING</text>
  <text class="brand-sub" x="85" y="334" font-size="24" textLength="379" lengthAdjust="spacingAndGlyphs">&amp; AIR-CONDITIONING</text>
  <text class="brand" x="85" y="373" font-size="36" textLength="379" lengthAdjust="spacingAndGlyphs">0400 555 127</text>

  <!-- products photo area -->
  <rect class="photo-products" role="img" aria-label="Photo of a hot water tank and a split air-conditioning unit with remote" x="40" y="414" width="366" height="326" rx="8" fill="#e4e8ec"/>

  <!-- stopwatch badge -->
  <g class="badge-stopwatch">
    <circle cx="635" cy="468" r="45" fill="var(--white)"/>
    <circle cx="642" cy="472" r="20" fill="none" stroke="#222" stroke-width="3"/>
    <rect x="637" y="444" width="10" height="6" rx="1" fill="#222"/>
    <path d="M642,460 V472 L650,478" fill="none" stroke="#222" stroke-width="3" stroke-linecap="round"/>
    <path d="M606,464 H616 M603,472 H614 M606,480 H616" stroke="#222" stroke-width="3" stroke-linecap="round"/>
  </g>

  <!-- 24/7 callout -->
  <text class="display" x="424" y="610" font-size="84" fill="var(--white)" textLength="226" lengthAdjust="spacingAndGlyphs">24/7</text>
  <text class="callout" x="667" y="566">EMERGENCY</text>
  <text class="callout" x="667" y="604">CALL OUT</text>

  <!-- offer -->
  <text class="display" x="40" y="857" font-size="52" fill="var(--blue)" textLength="279" lengthAdjust="spacingAndGlyphs">$30 OFF</text>
  <text class="body" x="178" y="896" font-size="24" text-anchor="middle">VOUCHER WHEN</text>
  <text class="body" x="178" y="930" font-size="24" text-anchor="middle">HPRODUCING THIS FLYER</text>
  <text class="body" x="178" y="961" font-size="16" text-anchor="middle">(LIMIT 1 PE HOUSE HOLD)</text>

  <!-- divider -->
  <line class="divider" x1="359" y1="731" x2="359" y2="1037" stroke="#9a9a9a" stroke-width="1" stroke-dasharray="3 3"/>

  <!-- services -->
  <text class="display" x="399" y="758" font-size="32" fill="var(--blue)" textLength="263" lengthAdjust="spacingAndGlyphs">WHAT WE DO</text>

  <g class="service-icon" fill="var(--blue)">
    <circle cx="421" cy="811" r="24"/><circle cx="604" cy="811" r="24"/>
    <circle cx="421" cy="884" r="24"/><circle cx="604" cy="884" r="24"/>
    <circle cx="421" cy="948" r="24"/><circle cx="604" cy="948" r="24"/>
    <circle cx="421" cy="1013" r="24"/>
  </g>
  <g class="service-glyph" fill="none" stroke="var(--white)" stroke-width="2" stroke-linecap="round">
    <path d="M411,822 V804 Q411,798 417,798 H423 Q428,798 428,804 V808 M406,822 H434"/>
    <path d="M594,802 V822 M599,802 V822 M604,802 V822 M609,802 V822 M614,802 V822 M590,812 H618"/>
    <rect x="413" y="874" width="16" height="22" rx="4"/><path d="M418,874 V869 H424 V874 M421,880 Q417,886 421,890 Q425,886 421,880"/>
    <circle cx="604" cy="884" r="12"/><path d="M596,880 H612 M596,884 H612 M596,888 H612"/>
    <path d="M407,958 L411,940 H431 L435,958 Z M414,940 L412,958 M421,940 V958 M428,940 L430,958 M409,949 H433"/>
    <rect x="590" y="938" width="28" height="12" rx="2"/><path d="M598,954 Q596,958 598,962 M604,954 Q602,958 604,962 M610,954 Q608,958 610,962"/>
    <circle cx="413" cy="1004" r="3"/><path d="M417,1024 L421,1008 H433 L429,1024 Z M425,1008 L423,1024"/>
  </g>

  <text class="service" x="459" y="807">Hot Water</text>
  <text class="service" x="459" y="836">System</text>
  <text class="service" x="641" y="807">Central</text>
  <text class="service" x="641" y="836">Heating</text>
  <text class="service" x="459" y="890">Gasfitting</text>
  <text class="service" x="641" y="890">Drainage</text>
  <text class="service" x="459" y="955">Roofing</text>
  <text class="service" x="641" y="955">Air-Conditioning</text>
  <text class="service" x="459" y="1009">Solar hot water systems/</text>
  <text class="service" x="459" y="1038">heat pump systems</text>

  <!-- footer -->
  <rect class="footer" x="300" y="1074" width="520" height="86" fill="var(--footer)"/>
  <path class="footer-dome" d="M0,1028 C60,1005 120,998 170,1000 C260,1005 310,1080 333,1160 H0 Z" fill="url(#dome)" stroke="var(--white)" stroke-width="6"/>

  <g class="phone-icon">
    <circle cx="155" cy="1059" r="20" fill="var(--white)"/>
    <path d="M148,1049 L153,1048 L156,1055 L153,1058 Q155,1064 160,1066 L163,1063 L169,1066 L168,1071 Q160,1073 152,1066 Q145,1058 148,1049 Z" fill="var(--blue)"/>
  </g>
  <text class="display" x="27" y="1126" font-size="30" fill="var(--white)" textLength="259" lengthAdjust="spacingAndGlyphs">0400555128</text>

  <g class="web-icon">
    <circle cx="367" cy="1117" r="14" fill="var(--blue)"/>
    <circle cx="367" cy="1117" r="8" fill="none" stroke="var(--white)" stroke-width="1.5"/>
    <path d="M359,1117 H375 M367,1109 Q362,1117 367,1125 Q372,1117 367,1109" fill="none" stroke="var(--white)" stroke-width="1.5"/>
  </g>
  <text class="contact" x="389" y="1123">7brinkplumbing.com</text>

  <g class="mail-icon">
    <circle cx="575" cy="1117" r="14" fill="var(--blue)"/>
    <rect x="567" y="1111" width="16" height="12" rx="1.5" fill="var(--white)"/>
    <path d="M567,1112 L575,1118 L583,1112" fill="none" stroke="var(--blue)" stroke-width="1.5"/>
  </g>
  <text class="contact" x="598" y="1123">sam@7brinkplumbing.com</text>
</svg>
</div>
</body>
</html>
```